Bahamas Pharmacy Requires Align Rx Flyer Re-Design

Hello,
We were so happy with your previous design we were hoping you'd be able to repair another design we had done. It's a half-letter single sided flyer (5.5 x 8) that promotes Align Remedies. The information on the first side of the attached PDF is unnecessary except for the "Are you taking more than 3 medications a day?" On the interior of the attached PDF, we'd like to keep as much information as possible. A diagram similar to the one at the top is necessary to make it easy to read. We trust your design style and are excited to see what you can bring. Please use the Coral Tide Pharmacy Logo, Twitter, and Facebook icons as you did on the "Heart Rate Tracker."
Updates
Target Market(s)
Mixed Race and African American families with elderly family members
Industry/Entity Type
Pharmacy
Requirements
Must have
- Any persons used should have a diverse range of backgrounds, preferably mixed race as most persons in the Bahamas are. They and their loved ones should be happy and relieved that they no longer need to worry about their medicines. If any couples are used they should be older and either mixed or african american.
Nice to have
- It's nice to have the diagram that explains what the "align rx" program does.
Should not have
- Too many fonts, colors or serif fonts.

```html
<!DOCTYPE html>
<html lang="en">
<head>
<meta charset="utf-8">
<title>Align Remedies – Coral Tide Pharmacy</title>
<link href="https://fonts.googleapis.com/css2?family=Open+Sans:ital,wght@0,300;0,400;0,600;0,700;1,300;1,400;1,700;1,800&display=swap" rel="stylesheet">
<style>
  :root {
    --brand-red: #c0272d;
    --brand-green: #2e8b3a;
    --band-green: #2f8a3c;
    --text-grey: #4a4a4a;
    --text-dark: #333333;
    --white: #ffffff;
    --photo-sky: #cfd9dc;
    --photo-warm: #e7b9a8;
    --photo-pink: #e58aa0;
    --pill-red: #e0443f;
    --pill-purple: #b07bd6;
    --pill-yellow: #f1c64a;
  }
  * { margin: 0; padding: 0; box-sizing: border-box; }
  html, body { width: 776px; height: 1200px; overflow: hidden; background: var(--white); }
  body { font-family: "Open Sans", Arial, sans-serif; color: var(--text-grey); font-weight: 300; }
  .flyer { position: relative; width: 776px; height: 1200px; overflow: hidden; background: var(--white); }

  .brand { position: absolute; top: 58px; left: 0; width: 776px; text-align: center; }
  .brand-name {
    display: inline-flex; align-items: center; gap: 12px;
    font-size: 27px; font-weight: 400; color: var(--brand-red);
    text-transform: uppercase; letter-spacing: 0.5px; line-height: 36px;
  }
  .brand-dot { width: 22px; height: 22px; border-radius: 50%; background: var(--brand-red); }

  .question-band {
    position: absolute; top: 150px; left: 0; width: 776px; height: 58px;
    background: var(--band-green); color: var(--white);
    font-size: 31px; font-style: italic; font-weight: 300;
    display: flex; align-items: center; justify-content: center; white-space: nowrap;
  }
  .question-band strong { font-weight: 800; margin: 0 7px; }

  .couple-photo {
    position: absolute; top: 208px; left: 0; width: 776px; height: 420px;
    background:
      radial-gradient(ellipse at 55% 45%, var(--photo-pink) 0%, rgba(229,138,160,0) 40%),
      radial-gradient(ellipse at 82% 40%, var(--photo-warm) 0%, rgba(231,185,168,0) 35%),
      linear-gradient(180deg, var(--photo-sky) 0%, #e9ecea 60%, var(--white) 100%);
  }
  .pills-photo {
    position: absolute; top: 930px; left: 0; width: 776px; height: 270px;
    background:
      radial-gradient(ellipse at 15% 80%, var(--pill-red) 0%, rgba(224,68,63,0) 30%),
      radial-gradient(ellipse at 70% 90%, var(--pill-purple) 0%, rgba(176,123,214,0) 30%),
      radial-gradient(ellipse at 45% 60%, var(--pill-yellow) 0%, rgba(241,198,74,0) 25%),
      linear-gradient(180deg, var(--white) 0%, #f3e6e6 40%, #eed9de 100%);
  }

  .intro-panel {
    position: absolute; top: 233px; left: 0; width: 420px; height: 218px;
    background: rgba(255,255,255,0.72);
  }
  .headline {
    position: absolute; top: 256px; left: 36px;
    font-size: 30px; font-weight: 700; color: var(--brand-red); line-height: 38px;
  }
  .intro {
    position: absolute; top: 320px; left: 36px;
    font-size: 20px; line-height: 26px; white-space: nowrap;
  }
  .details {
    position: absolute; top: 472px; left: 36px;
    font-size: 20px; line-height: 26px; white-space: nowrap;
  }
  .benefits {
    position: absolute; top: 577px; left: 36px; list-style: none;
    font-size: 20px; line-height: 26px; white-space: nowrap;
  }
  .benefits li { position: relative; padding-left: 14px; margin-bottom: 5.5px; }
  .benefits li::before { content: "•"; position: absolute; left: 0; }

  .step {
    position: absolute; border-radius: 50%; border: 3px solid #d9d9d9;
    box-shadow: 0 2px 6px rgba(0,0,0,0.2);
  }
  .step-tray { left: 508px; top: 440px; width: 240px; height: 240px;
    background: radial-gradient(circle at 50% 55%, #3b62b8 0%, #3b62b8 45%, #e04a3a 70%, var(--white) 72%); }
  .step-blister { left: 442px; top: 598px; width: 240px; height: 240px;
    background: radial-gradient(circle at 40% 45%, #dfe3ea 0%, #c9ccd4 45%, #e7c7b0 70%, var(--white) 74%); }
  .step-pouch { left: 512px; top: 780px; width: 250px; height: 250px;
    background: radial-gradient(circle at 45% 45%, #e9e9e9 0%, #d8d8d8 40%, #f2a64a 55%, var(--white) 70%); }
  .flow-arrows { position: absolute; left: 0; top: 0; width: 776px; height: 1200px; pointer-events: none; }

  .signup-band {
    position: absolute; top: 1004px; left: 0; width: 776px; height: 88px;
    background: rgba(255,255,255,0.82); text-align: center;
    font-size: 20px; padding-top: 33px; line-height: 25px;
  }
  .signup-band strong { font-weight: 700; color: var(--text-dark); }
  .signup-band .web { font-style: italic; font-weight: 700; color: var(--text-dark); }
  .motto {
    position: absolute; top: 1099px; left: 0; width: 776px; text-align: center;
    font-size: 31px; font-style: italic; font-weight: 700; color: var(--brand-green); line-height: 42px;
  }
</style>
</head>
<body>
<main class="flyer">
  <header class="brand">
    <div class="brand-name"><span class="brand-dot"></span>Coral Tide Pharmacy</div>
  </header>

  <div class="question-band">Are you taking <strong>3 or more</strong> medications each day?</div>

  <div class="couple-photo" role="img" aria-label="Smiling older couple outdoors on a sunny day"></div>
  <div class="pills-photo" role="img" aria-label="Close-up of colourful medication capsules"></div>

  <div class="intro-panel"></div>
  <h1 class="headline">Align Remedies</h1>
  <p class="intro">Save time and trouble by<br>having all your prescriptions<br>refilled at the same time<br>each month.</p>
  <p class="details">Align Rx is easy and convenient.<br>Your enrollment simplifies all your<br>medications in one convenient packaging:</p>

  <ul class="benefits">
    <li>No need to call in prescription refills</li>
    <li>Fewer trips to the pharmacy</li>
    <li>No worries about running out of<br>your medication</li>
    <li>Prescription ready on your refill date</li>
    <li>All your daily medications organized<br>by time of day</li>
    <li>Correct dose always at your fingertips</li>
    <li>Convenient dose reminder system to<br>get the best results possible from<br>your medications</li>
    <li>One week prior to your prescriptions<br>being refilled we call you to verify<br>what is needed</li>
  </ul>

  <div class="step step-tray" role="img" aria-label="Blister card of daily medications organized by time of day"></div>
  <div class="step step-blister" role="img" aria-label="Hand taking a dose from a blister pack"></div>
  <div class="step step-pouch" role="img" aria-label="Labelled single-dose pouch with tablets"></div>

  <svg class="flow-arrows" viewBox="0 0 776 1200" aria-hidden="true">
    <g fill="none" stroke="var(--brand-red)" stroke-width="5" stroke-linecap="round">
      <path d="M738 660 Q735 710 690 740"/>
      <path d="M450 812 Q455 870 495 900"/>
    </g>
    <g fill="var(--brand-red)">
      <path d="M678 748 L700 728 L704 750 Z"/>
      <path d="M505 908 L482 900 L498 884 Z"/>
    </g>
  </svg>

  <div class="signup-band">
    <p>Speak to the pharmacist about signing up for this program. <strong>It’s FREE!</strong></p>
    <p class="web">www.coraltidepharmacy.com</p>
  </div>
  <p class="motto">Right Med. Right Dose. Right Time.</p>
</main>
</body>
</html>
```